Harbour Wing Flights business card

I need a business card designed based on our logo -- designed by Studio Flock designers.

The logo is to be taken from our web site at www.harbourwingflights.com.au

I need to have this card designed quickly as its needed for business meetings
Updates

Hi Designers, Please see my updated brief for my business card. I have attached logo images and a brochure for inspiration... Regards, Gavin Trelford Harbour Wing Flights

Target Market(s)

Hotel owners and operators (concierge) and tourists to Australia

Industry/Entity Type

Business

Font styles to use
Sans Serif

Colors
84abd2
3176b5
85abd2
cedeec

Requirements
Must have
• Utilise our logo. Found on our web page www.harbourwingflights.com.au

SIDE 1
Must have my name: Gavin Trelford
Title:Owner
Phone number: 1300 418 396
Mobile:0461273958

SIDE 2
LOGO
PREPARE TO BE AMAZED! (see attached brochure for information and font style)
Nice to have
• Something that reflects aviation and tour with a light aircraft

```html
<!DOCTYPE html>
<html lang="en">
<head>
<meta charset="utf-8">
<title>Harbour Wing Flights – Business Card</title>
<link href="https://fonts.googleapis.com/css2?family=Open+Sans:wght@400;600&family=Russo+One&display=swap" rel="stylesheet">
<style>
  :root {
    --brand-blue: #3176b5;
    --mid-blue: #84abd2;
    --soft-blue: #85abd2;
    --pale-blue: #cedeec;
    --swoosh-white: #f2f5f9;
    --ink: #2f3338;
    --stage: #e9edf1;
    --harbour-deep: #1f56b8;
    --harbour-sky: #dfe9f3;
  }
  * { box-sizing: border-box; margin: 0; padding: 0; }
  html, body { width: 1200px; height: 675px; overflow: hidden; }
  body {
    background: var(--stage);
    font-family: "Open Sans", Arial, sans-serif;
    position: relative;
  }
  .card {
    position: absolute;
    top: 190px;
    width: 520px;
    height: 290px;
    overflow: hidden;
    box-shadow: 0 6px 18px rgba(0,0,0,0.18);
  }
  .card--front { left: 50px; background: var(--brand-blue); }
  .card--back  { left: 630px; }

  .card__art { position: absolute; inset: 0; width: 100%; height: 100%; }

  .brand-mark {
    position: absolute;
    left: 24px;
    top: 146px;
    color: #ffffff;
    font-weight: 600;
    font-size: 11px;
    line-height: 14px;
    letter-spacing: 0.5px;
    text-transform: uppercase;
  }
  .slogan {
    position: absolute;
    left: 22px;
    top: 166px;
    width: 270px;
    font-family: "Russo One", Arial, sans-serif;
    font-size: 27px;
    line-height: 1.25;
    color: var(--pale-blue);
    text-transform: uppercase;
  }
  .tagline {
    position: absolute;
    right: 20px;
    top: 206px;
    text-align: right;
    text-transform: uppercase;
    font-size: 18px;
    line-height: 1.3;
    letter-spacing: 1.5px;
  }
  .tagline__lead { color: var(--brand-blue); display: block; }
  .tagline__rest { color: var(--ink); display: block; }

  .company-name {
    position: absolute;
    top: 64px;
    left: 160px;
    right: 10px;
    text-align: center;
    font-size: 26px;
    font-weight: 400;
    letter-spacing: 1px;
    text-transform: uppercase;
    color: var(--brand-blue);
  }
  .contact {
    position: absolute;
    left: 190px;
    top: 172px;
    display: grid;
    grid-template-columns: auto auto;
    column-gap: 8px;
    color: var(--ink);
    text-transform: uppercase;
    font-size: 17px;
    line-height: 1.2;
    letter-spacing: 0.5px;
  }
  .contact__label { text-align: right; }
  .contact__label--small { font-size: 12px; align-self: center; }
</style>
</head>
<body>

<section class="card card--front" aria-label="Card front">
  <svg class="card__art" viewBox="0 0 520 290" role="img" aria-label="Aerial photograph of Sydney Harbour and city skyline with a light aircraft in flight">
    <defs>
      <linearGradient id="harbourPhoto" x1="0" y1="0" x2="1" y2="1">
        <stop offset="0" stop-color="#c9d3dc"/>
        <stop offset="0.45" stop-color="var(--harbour-deep)"/>
        <stop offset="1" stop-color="#3f86d0"/>
      </linearGradient>
    </defs>
    <path d="M0,0 H520 V110 C400,140 220,150 0,134 Z" fill="url(#harbourPhoto)"/>
  </svg>
  <svg class="card__art" viewBox="0 0 520 290" aria-hidden="true">
    <path d="M150,290 C260,215 380,165 520,140 V290 Z" fill="var(--swoosh-white)"/>
  </svg>

  <div class="brand-mark">Harbour Wing Flights</div>
  <p class="slogan">Prepare to be amazed!</p>
  <p class="tagline">
    <span class="tagline__lead">Fly over Sydney</span>
    <span class="tagline__rest">in an aircraft</span>
  </p>
</section>

<section class="card card--back" aria-label="Card back">
  <svg class="card__art" viewBox="0 0 520 290" role="img" aria-label="Faded aerial view of the city with a light aircraft above the company name">
    <defs>
      <linearGradient id="cityFade" x1="0" y1="0" x2="0" y2="1">
        <stop offset="0" stop-color="var(--harbour-sky)"/>
        <stop offset="1" stop-color="var(--pale-blue)"/>
      </linearGradient>
    </defs>
    <rect width="520" height="290" fill="url(#cityFade)"/>
  </svg>
  <svg class="card__art" viewBox="0 0 520 290" aria-hidden="true">
    <rect x="0" y="0" width="150" height="175" fill="var(--mid-blue)" opacity="0.55"/>
    <rect x="0" y="175" width="150" height="100" fill="var(--brand-blue)"/>
  </svg>

  <h1 class="company-name">Harbour Wing Flights</h1>

  <dl class="contact">
    <dt class="contact__label">Name:</dt><dd>Gavin Trelford</dd>
    <dt class="contact__label">Title:</dt><dd>Owner</dd>
    <dt class="contact__label contact__label--small">Phone number:</dt><dd>1300 418 396</dd>
    <dt class="contact__label">Mobile:</dt><dd>0461273958</dd>
  </dl>
</section>

</body>
</html>
```